Technical Communications firm needs an article turned into a white paper

We want to redesign a 3-part blog series into a white paper that we can print for a conference. I've consolidated the three posts into the attached Word document.

We are looking for a light, easy to read design. Good use of graphics to support the message. I've added the graphics we used in the original post.

You can view them at
http://www.quillmarrowgroup.com/blog/are-you-satisfied-with-your-dita-solution/

Target Market(s)

Product managers from High-tech, Finance, and Medical industries.

Industry/Entity Type

Information Technology

Colors

Designer to choose colors to be used in the design.

Requirements
Must have
• Must be modern, light, easy to read and slick design. Try to incorporate the graphics provided, but feel free to add more. Must retain the lists and tables.
• Must align with our website/brand.
• Must be easy to read. So not too busy.
• Please move all footnotes to endnotes. You'll need to rework the numbering.
Nice to have
• Awesome coverpage.
Should not have
• Hokey clipart. Not too heavy or hard to read.

```html
<!DOCTYPE html>
<html lang="en">
<head>
<meta charset="utf-8">
<title>White Paper – Page 8</title>
<link href="https://fonts.googleapis.com/css2?family=Carlito:wght@400;700&family=Open+Sans:wght@400;700&display=swap" rel="stylesheet">
<style>
  :root {
    --navy: #1c1c9e;
    --cyan: #1ba9e1;
    --ink: #262626;
    --rule: #9fc7e6;
    --frame: #c9c9c9;
    --paper: #ffffff;
  }
  * { margin: 0; padding: 0; box-sizing: border-box; }
  html, body { width: 927px; height: 1200px; overflow: hidden; background: var(--paper); }
  .page {
    position: relative; width: 927px; height: 1200px;
    border: 1px solid var(--frame); background: var(--paper);
    font-family: "Carlito", "Calibri", sans-serif; color: var(--ink);
  }
  .brand { position: absolute; left: 84px; top: 58px; display: flex; align-items: center; gap: 12px; }
  .brand-dot { width: 78px; height: 78px; border-radius: 50%; background: var(--navy); }
  .brand-name {
    font-family: "Open Sans", sans-serif; font-weight: 700; font-size: 22px;
    line-height: 24px; color: var(--navy); letter-spacing: 0.5px;
  }
  .spine { position: absolute; left: 111px; top: 144px; width: 3px; height: 916px; background: var(--navy); }
  .page-number {
    position: absolute; left: 744px; top: 70px; width: 126px; height: 28px;
    border-top: 1px solid var(--rule); border-bottom: 1px solid var(--rule);
    font-family: "Open Sans", sans-serif; font-weight: 700; font-size: 15px;
    color: var(--navy); text-align: center; line-height: 27px; letter-spacing: 1px;
  }
  .content { position: absolute; left: 178px; width: 693px; }
  .lead {
    font-family: "Open Sans", sans-serif; font-size: 14.6px; line-height: 18.4px;
    text-align: center; top: 166px;
  }
  p.body { font-size: 16px; line-height: 22.4px; text-align: justify; }
  p.indent { text-indent: 29px; }
  .section-title {
    font-family: "Open Sans", sans-serif; font-weight: 700; font-size: 31px;
    color: var(--navy); text-decoration: underline; text-decoration-thickness: 2px;
    text-underline-offset: 4px; text-align: center; line-height: 40px;
  }
  .checklist { list-style: none; position: absolute; left: 236px; width: 635px; top: 566px; }
  .checklist li {
    position: relative; padding-left: 31px; font-size: 16px; line-height: 24px;
    margin-bottom: 0.3px; text-align: justify;
  }
  .checklist li::before {
    content: ""; position: absolute; left: 0; top: 9px; width: 6px; height: 6px;
    border-radius: 50%; background: var(--ink);
  }
  .checklist .term { color: var(--navy); font-weight: 700; text-decoration: underline; }
  .dot-rule { position: absolute; left: 105px; top: 1071px; }
</style>
</head>
<body>
<div class="page">
  <div class="brand">
    <div class="brand-dot"></div>
    <div class="brand-name">QUILL MARROW<br>GROUP</div>
  </div>
  <div class="page-number">PAGE 8</div>
  <div class="spine"></div>

  <div class="content lead">
    into an entirely new system with relatively minor disruption. Or if your entire system isn’t the problem, you can often replace components of your solution with components from other vendors to achieve a better result. Lastly, because your content is in XML, it can often be re-factored to correct problems that have accumulated in your content over time.
  </div>
  <p class="content body" style="top:240px;">Before we look at changing your technology, we should examine some of these problems to see if we can identify a more appropriate root cause.</p>

  <h2 class="content section-title" style="top:315px;">Performance Problems</h2>
  <p class="content body indent" style="top:360px;">Common complaints regarding performance include observations that processes take longer or systems are slower to respond than they were before the move to DITA. Part of this observation may be related to aligning to different expectations. You are working with a lot more parts and potentially with many more people to get the job done. Some parts of the process will naturally take longer. These perceived issues will appear worse when you are required to collaborate with writers, editors, and other team members across great distances.</p>
  <p class="content body" style="top:496px;">If the overall time and effort does not significantly improve over the course of 2-3 production life cycles of the content, then there may be some other issues at play. You’ll want to examine your:</p>

  <ul class="checklist">
    <li><span class="term">Processes</span> – Have you eliminated redundant activities in your processes?</li>
    <li><span class="term">Pipes</span> – Is your productivity impeded by network performance?</li>
    <li><span class="term">Platforms</span> – Are users experiencing problems related to disparate desktop configurations?</li>
    <li><span class="term">Processors</span> – Are your servers or client machines underpowered for the tools?</li>
    <li><span class="term">People</span> – Do your users follow established best practices for working with your tools?</li>
  </ul>

  <p class="content body indent" style="top:737px;">Once you’ve identified all external factors affecting performance, you’ll want to examine how your tools are configured and deployed. There may be alternative features, configurations, or components that will greatly improve system performance. Your tool vendors or service providers should be able to help you examine your options.</p>

  <h2 class="content section-title" style="top:849px;">Complexity Problems</h2>
  <p class="content body indent" style="top:894px;">Finding the correct balance of complexity versus utility is one of the biggest challenges we face in DITA deployments. The problem may not be that your tools are too complex, rather that too much complexity is exposed to the wrong group of users. The best-architected systems attempt to push the most complexity onto the shoulders of the fewest number of people. As much as possible, let the software handle most of the heavy lifting.</p>

  <svg class="dot-rule" width="766" height="16" viewBox="0 0 766 16" aria-hidden="true">
    <g>
      <circle cx="7" cy="7" r="6.5" fill="var(--navy)"/><circle cx="30" cy="7" r="6.5" fill="var(--cyan)"/>
      <circle cx="53" cy="7" r="6.5" fill="var(--navy)"/><circle cx="76" cy="7" r="6.5" fill="var(--cyan)"/>
      <circle cx="99" cy="7" r="6.5" fill="var(--navy)"/><circle cx="122" cy="7" r="6.5" fill="var(--cyan)"/>
      <circle cx="145" cy="7" r="6.5" fill="var(--navy)"/><circle cx="168" cy="7" r="6.5" fill="var(--cyan)"/>
      <circle cx="191" cy="7" r="6.5" fill="var(--navy)"/><circle cx="214" cy="7" r="6.5" fill="var(--cyan)"/>
      <circle cx="237" cy="7" r="6.5" fill="var(--navy)"/><circle cx="260" cy="7" r="6.5" fill="var(--cyan)"/>
      <circle cx="283" cy="7" r="6.5" fill="var(--navy)"/><circle cx="306" cy="7" r="6.5" fill="var(--cyan)"/>
      <circle cx="329" cy="7" r="6.5" fill="var(--navy)"/><circle cx="352" cy="7" r="6.5" fill="var(--cyan)"/>
      <circle cx="375" cy="7" r="6.5" fill="var(--navy)"/><circle cx="398" cy="7" r="6.5" fill="var(--cyan)"/>
      <circle cx="421" cy="7" r="6.5" fill="var(--navy)"/><circle cx="444" cy="7" r="6.5" fill="var(--cyan)"/>
      <circle cx="467" cy="7" r="6.5" fill="var(--navy)"/><circle cx="490" cy="7" r="6.5" fill="var(--cyan)"/>
      <circle cx="513" cy="7" r="6.5" fill="var(--navy)"/><circle cx="536" cy="7" r="6.5" fill="var(--cyan)"/>
      <circle cx="559" cy="7" r="6.5" fill="var(--navy)"/><circle cx="582" cy="7" r="6.5" fill="var(--cyan)"/>
      <circle cx="605" cy="7" r="6.5" fill="var(--navy)"/><circle cx="628" cy="7" r="6.5" fill="var(--cyan)"/>
      <circle cx="651" cy="7" r="6.5" fill="var(--navy)"/><circle cx="674" cy="7" r="6.5" fill="var(--cyan)"/>
      <circle cx="697" cy="7" r="6.5" fill="var(--navy)"/><circle cx="720" cy="7" r="6.5" fill="var(--cyan)"/>
      <circle cx="743" cy="7" r="6.5" fill="var(--navy)"/>
    </g>
  </svg>
</div>
</body>
</html>
```